Health care technology software systems

We have a solid logo. We have company colors that will need to be used as well. We just need a great business card design. We sell to health plans but want to be modern
Updates

Need extra days to review

Target Market(s)

Health technology sector selling into Health Plans

Industry/Entity Type

Health Care Technology

Contact Information for Business Card

Name, title, address, phone number, email

Requirements
Must have
• Use of Kembrata corporate colors - Uploaded w/ our logos

```html
<!DOCTYPE html>
<html lang="en">
<head>
<meta charset="utf-8">
<title>Kembrata Business Card</title>
<link href="https://fonts.googleapis.com/css2?family=Questrial&family=Arimo:wght@400&display=swap" rel="stylesheet">
<style>
  :root {
    --page: #1e1e1e;
    --card-dark: #363835;
    --paper: #ffffff;
    --brand-green: #8cc21f;
    --brand-blue: #00a4e0;
    --ink: #3a3a3a;
    --text-light: #ffffff;
  }
  * { margin: 0; padding: 0; box-sizing: border-box; }
  html, body { width: 1200px; height: 1015px; overflow: hidden; }
  body {
    background: radial-gradient(ellipse at center, #3a3a3a 0%, var(--page) 75%);
    position: relative;
    font-family: "Arimo", Arial, sans-serif;
  }
  .card {
    position: absolute;
    left: 220px;
    width: 760px;
    height: 434px;
    overflow: hidden;
    box-shadow: 0 14px 30px rgba(0,0,0,0.55);
  }
  .card-back { top: 40px; background: var(--card-dark); }
  .card-front { top: 540px; }
  .card-art { position: absolute; inset: 0; }

  .wordmark {
    position: absolute;
    display: flex;
    align-items: center;
    font-family: "Questrial", "Century Gothic", sans-serif;
    white-space: nowrap;
    line-height: 1;
  }
  .wordmark-dot { border-radius: 50%; background: var(--brand-blue); flex: none; }
  .card-back .wordmark {
    left: 0; right: 0; top: 170px;
    justify-content: center; gap: 26px;
    font-size: 88px; letter-spacing: 2px; color: var(--text-light);
  }
  .card-back .wordmark-dot { width: 66px; height: 66px; }
  .card-front .wordmark {
    left: 478px; top: 158px; gap: 12px;
    font-size: 42px; letter-spacing: 1px; color: var(--ink);
  }
  .card-front .wordmark-dot { width: 34px; height: 34px; }

  .person { position: absolute; left: 44px; top: 62px; }
  .person-name {
    font-family: "Questrial", "Century Gothic", sans-serif;
    font-size: 36px; color: var(--brand-green); line-height: 1;
  }
  .person-title { font-size: 18px; color: var(--text-light); margin-top: 6px; }

  .contact-list { position: absolute; left: 60px; top: 176px; list-style: none; }
  .contact-list li {
    display: flex; align-items: center; gap: 10px;
    font-size: 18px; color: var(--text-light); line-height: 28px;
  }
  .contact-list svg { width: 18px; height: 18px; flex: none; }
  .accent { color: var(--brand-green); }

  .address {
    position: absolute; left: 60px; top: 300px;
    font-style: normal; font-size: 18px; line-height: 26px; color: var(--text-light);
  }
</style>
</head>
<body>

  <section class="card card-back" aria-label="Card back">
    <div class="wordmark"><span class="wordmark-dot"></span><span>kembrata</span></div>
  </section>

  <section class="card card-front" aria-label="Card front">
    <svg class="card-art" viewBox="0 0 760 434" preserveAspectRatio="none" aria-hidden="true">
      <rect width="760" height="434" fill="var(--card-dark)"/>
      <path d="M430,0 C392,120 400,290 760,410 L760,0 Z" fill="var(--paper)"/>
      <path d="M418,0 C378,125 392,300 745,420" fill="none" stroke="var(--brand-green)" stroke-width="7"/>
      <path d="M448,130 C452,270 560,360 760,402" fill="none" stroke="var(--brand-blue)" stroke-width="9"/>
    </svg>

    <div class="person">
      <p class="person-name">Daniel Reyes</p>
      <p class="person-title">Managing Director</p>
    </div>

    <ul class="contact-list">
      <li>
        <svg viewBox="0 0 24 24" aria-hidden="true"><path fill="var(--brand-green)" d="M6.6 10.8a15 15 0 0 0 6.6 6.6l2.2-2.2a1 1 0 0 1 1-.25 11.4 11.4 0 0 0 3.6.57 1 1 0 0 1 1 1V20a1 1 0 0 1-1 1A17 17 0 0 1 3 4a1 1 0 0 1 1-1h3.5a1 1 0 0 1 1 1c0 1.25.2 2.45.57 3.57a1 1 0 0 1-.25 1z"/></svg>
        <span>044-987 654 321</span>
      </li>
      <li>
        <svg viewBox="0 0 24 24" aria-hidden="true"><rect x="2" y="5" width="20" height="14" fill="var(--brand-green)"/><path d="M2 5l10 8 10-8" fill="none" stroke="var(--card-dark)" stroke-width="1.6"/></svg>
        <span>info@kembrata.com</span>
      </li>
      <li>
        <svg viewBox="0 0 24 24" aria-hidden="true"><g fill="none" stroke="var(--brand-green)" stroke-width="2"><circle cx="12" cy="12" r="9.5"/><ellipse cx="12" cy="12" rx="4" ry="9.5"/><path d="M2.5 12h19M4 7h16M4 17h16"/></g></svg>
        <span>www.<span class="accent">kembrata</span>.com</span>
      </li>
    </ul>

    <address class="address">421, Address line goes here<br>45452, Country Name</address>

    <div class="wordmark"><span class="wordmark-dot"></span><span>kembrata</span></div>
  </section>

</body>
</html>
```